Modern and strong website design for a Dutch crowdsourcing company
.

We are startup company providing crowdsourcing of administrative and customers service tasks for larger companies and other organizations. We offer cost savings and scale-ability combined with higher quality of execution. We will soon enter the market and need a website that has two major target groups: 1. Our corporate customers 2. The mainly younger crowd executing the tasks on our platform.
The target group of customers are Influencers and decision makers with companies and other organizations in with large administrative and customer service departments. Most information in the startup phase will be targeting this group.
The target group of future crowd workers will be heterogeneous, from students to stay at home mums or night shift workers who want to earn some extra money by performing easy to execute microtasks in the cloud. We will target both Dutch and international workers.

The website must be developed for browsing on a computer but also be optimized for mobile devices and tablets.
The website must be optimized and tested for the major browsers on windows, macOS and mobile devices.

For the minimum requirement for the website see attached wireframes

The present landing page http://thepinegladeloft.com and logo are not reflecting our preferences!
See enclosed a new logo that stands for both the crowdwork (performed for our customers) and the crowd (the pine glade loft).

Target Market(s)

see tekst above.

Industry/Entity Type

Business Service

Coding

Coded - Design and coding required

Number of Pages Required

5+ page

Font styles to use
Sans Serif
Other font styles liked:
• Lato, Open Sans

Colors

Designer to choose colors to be used in the design.

Requirements
Must have
• start devider screen
• home page displaying business and worker information
• a page displaying only info for businesses
• a page displaying only info for workers
• a contact form
• a reviews page
• color scheme from logo
• responsiveness!
Nice to have
• Nice animations
• overlapping blocks, animated on scroll
• lightbox effects if applicable
• animated mobile menu icon and menu itself

```html
<!DOCTYPE html>
<html lang="en">
<head>
<meta charset="utf-8">
<title>The Pine Glade Loft</title>
<link rel="stylesheet" href="https://fonts.googleapis.com/css2?family=Lato:wght@400;700&family=Raleway:wght@700&display=swap">
<style>
  :root {
    --brand-orange: #f07b05;
    --brand-grey: #7f7f80;
    --button-dark: #585858;
    --button-dark-border: #2e2e2e;
    --text-light: #ffffff;
    --hero-top: #b9c4cc;
    --hero-mid: #8f9aa3;
    --hero-bottom: #a9b0b4;
  }
  * { box-sizing: border-box; margin: 0; padding: 0; }
  html, body {
    width: 1200px;
    height: 697px;
    overflow: hidden;
    font-family: "Lato", sans-serif;
  }
  .splash {
    position: relative;
    width: 1200px;
    height: 697px;
    overflow: hidden;
  }
  .splash-backdrop {
    position: absolute;
    inset: 0;
    background:
      radial-gradient(ellipse 420px 200px at 600px 360px, rgba(150, 110, 90, 0.55), transparent 70%),
      linear-gradient(90deg, rgba(110, 120, 130, 0.55) 0%, transparent 30%, transparent 72%, rgba(120, 130, 140, 0.55) 100%),
      linear-gradient(180deg, var(--hero-top) 0%, var(--hero-mid) 55%, var(--hero-bottom) 100%);
  }
  .splash-content {
    position: absolute;
    inset: 0;
    text-align: center;
  }
  .brand-name {
    position: absolute;
    top: 180px;
    left: 0;
    width: 100%;
    font-family: "Raleway", sans-serif;
    font-weight: 700;
    font-size: 84px;
    line-height: 1;
    color: var(--brand-orange);
    letter-spacing: -1px;
  }
  .splash-title {
    position: absolute;
    top: 420px;
    left: 0;
    width: 100%;
    font-family: "Raleway", sans-serif;
    font-weight: 700;
    font-size: 27px;
    color: var(--text-light);
  }
  .splash-subtitle {
    position: absolute;
    top: 476px;
    left: 0;
    width: 100%;
    font-family: "Raleway", sans-serif;
    font-weight: 700;
    font-size: 40px;
    color: var(--text-light);
  }
  .audience-choice {
    position: absolute;
    top: 570px;
    left: 383px;
    display: flex;
    gap: 26px;
  }
  .audience-button {
    display: flex;
    align-items: center;
    justify-content: center;
    width: 203px;
    height: 50px;
    font-size: 16px;
    color: var(--text-light);
    text-decoration: none;
  }
  .audience-button--workers {
    background: var(--button-dark);
    border: 1px solid var(--button-dark-border);
    font-weight: 700;
  }
  .audience-button--businesses {
    background: var(--brand-orange);
    border: 1px solid var(--text-light);
    font-weight: 400;
  }
</style>
</head>
<body>
  <main class="splash">
    <div class="splash-backdrop" role="img" aria-label="Photo of two business people in suits shaking hands in a bright office"></div>
    <div class="splash-content">
      <h1 class="brand-name">The Pine Glade Loft</h1>
      <p class="splash-title">Pine Glade Loft</p>
      <p class="splash-subtitle">For</p>
      <nav class="audience-choice">
        <a class="audience-button audience-button--workers" href="#workers">Workers</a>
        <a class="audience-button audience-button--businesses" href="#businesses">Businesses</a>
      </nav>
    </div>
  </main>
</body>
</html>
```